Smart, intuitive SaaS software dashboard design

PactBloom is an innovative modern SaaS (software as a service) solution for contract and meeting management.

What we are looking for is fresh ideas for our dashboard. We do not need web coding or actionable wireframes now – but purely great design ideas from where to continue forward.

How should a modern web software dashboard look like? Fresh, intuitive, easy-to-use, and adaptable for responsive mobile designs. We hope that when the user logs into the service and sees the dashboard, he/she gets a good big picture of the current status of the most important documents of his/hers company.

To get to know the service and see the components, we kindly ask you to register to our service at www.pactbloom-demo.net and to utilize the free trial (30 days) so you can see the existing dashboard live. And also try out how it works. Might help you to get ideas how to improve it.

(The designer we will choose might be offered later on to design some other pages as well (contract view and edit pages, meeting page etc).)

You’ll find additional information in the attachment.

You’ll find more information of the company and the service also at www.pactbloom-demo.net

Target Market(s)

Global

Industry/Entity Type

Business Management

Number of Pages Required

1 page

Font styles to use
Sans Serif

Requirements
Must have
• 1) Clear design idea for us to iterate from, 2) Modern look and feel - elegant & bold at the same time - still with credibility in our target group. And 3) Suitable for dashboard usage - it should it a clear big picture for the user.
• UPDATE:
• Users should see most important things with one glance. Therefore we would like to see AT LEAST these items mentioned below on the first page.
• NOTE: if all these things are visible on the dashboard, the menu list is maybe not needed on the left. (And there might be some icons on the top header with needed settings/inbox features anyway.)
• NOTE2: as explained earlier, the design should be responsive i.e. work without modifications in PC, iPad and mobile (the areas/boxes would just rearrange themselves on top of each other.)
• -First area should be Documents, which would include different document categories: Contracts, Finance & Admin and HR
• -All different types of Meetings could be the next area (upcoming ones clearly visible with date and maybe description, time and location visible also).
• -Reminders and Activity Feed (they might also be together in top of each other, so that Reminder is visible first and Activity feed can be chosen from the tab.)
• -Virtual Datarooms (maybe 1-3 different ones with some analytics for each visible e.g. like usage/visits per day)
• Saved searches in very important list as users can save their most important searches. There are typically many of these, so at least 5 should be visible and then see all button (maybe even more could be visible if they fit on your design)
• My Latest is also important.
• (As explained, Action Required area is NOT needed anymore).
Nice to have
• Surprise us!
Should not have
• Please avoid the boring traditional legacy stuff and the common report dashboards.
• You do not need design a 100% mockup for the techie to continue with. The ideas count.

```html
<!DOCTYPE html>
<html lang="en">
<head>
<meta charset="utf-8">
<title>PactBloom Dashboard</title>
<link rel="stylesheet" href="https://fonts.googleapis.com/css2?family=Open+Sans:ital,wght@0,400;0,600;0,700;1,400&display=swap">
<style>
:root{
  --blue:#2c6db4;
  --blue-dark:#1f5ea3;
  --blue-tag:#0d58a6;
  --ink:#2f3338;
  --muted:#7a7f85;
  --line:#dcdcdc;
  --page:#e8e8e8;
  --panel:#ffffff;
  --tab-off:#e6e6e6;
  --green:#3aa55c;
  --red:#f0506e;
  --orange:#f5a033;
  --black:#000000;
}
*{box-sizing:border-box;margin:0;padding:0}
html,body{width:1200px;height:900px;overflow:hidden}
body{font-family:"Open Sans",Arial,sans-serif;color:var(--ink);background:var(--page);position:relative}
.abs{position:absolute}

/* Top bar */
.topbar{position:absolute;left:0;top:0;width:1200px;height:76px;background:linear-gradient(90deg,#2b6cb3,#2f72b9)}
.brand{position:absolute;left:0;top:0;width:240px;height:76px;background:var(--black);display:flex;align-items:center;padding-left:20px;gap:10px}
.brand-dot{width:34px;height:34px;border-radius:50%;background:#ffffff}
.brand-name{color:#fff;font-size:21px;font-weight:600;letter-spacing:.5px}
.add-btn{left:254px;top:29px;width:18px;height:18px;border-radius:50%;background:#fff;color:var(--blue);font-weight:700;font-size:16px;line-height:17px;text-align:center}
.nav-link{top:26px;color:#fff;font-style:italic;font-size:15px}
.nav-caret{display:inline-block;margin-left:8px;width:0;height:0;border-left:6px solid transparent;border-right:6px solid transparent;border-top:7px solid #dfe9f5;vertical-align:middle}
.nav-sep{left:433px;top:28px;width:1px;height:20px;background:#8fb3dc}
.nav-underline{left:300px;top:52px;width:512px;height:1px;background:#7ea6d5}
.chat-badge{left:874px;top:18px;width:18px;height:13px;border-radius:7px;background:#f3d11b;color:#333;font-size:9px;font-weight:700;text-align:center;line-height:13px}
.greet{left:914px;top:27px;color:#fff;font-size:15px}
.greet b{font-weight:700}
.avatar{left:1005px;top:14px;width:50px;height:50px;border-radius:50%;background:#d8d8d8;border:2px solid #fff}
.logout{left:1070px;top:27px;color:#fff;font-size:15px;display:flex;align-items:center;gap:6px}

/* Side rail */
.rail{position:absolute;left:0;top:76px;width:60px;height:774px;background:linear-gradient(180deg,#2b6cb3,#2d6fb6)}
.rail-item{width:60px;height:61px;border-bottom:1px solid #255f9f;display:flex;align-items:center;justify-content:center}

/* Panels */
.panel{position:absolute;background:var(--panel);border:1px solid #d6d6d6}
.panel-title{font-size:20px;color:var(--blue);padding:12px 0 0 15px;height:53px;border-bottom:1px solid var(--line)}
.docs{left:61px;top:77px;width:396px;height:421px}
.meet{left:469px;top:77px;width:397px;height:421px}
.rem{left:877px;top:77px;width:322px;height:421px}
.latest{left:70px;top:507px;width:1120px;height:334px}

/* Documents */
.doc-tabs{position:absolute;left:0;top:53px;width:396px;height:92px;display:flex;border-bottom:1px solid var(--line)}
.doc-tab{flex:1;background:var(--tab-off);display:flex;flex-direction:column;align-items:center;justify-content:center;gap:6px;font-size:14px;color:#555;font-weight:600;border-left:1px solid #d4d4d4}
.doc-tab.active{background:#fff;color:var(--ink);border-left:none;position:relative}
.doc-tab.active::after{content:"";position:absolute;bottom:-8px;left:50%;margin-left:-8px;width:14px;height:14px;background:#fff;border-right:1px solid var(--line);border-bottom:1px solid var(--line);transform:rotate(45deg)}
.doc-row{position:absolute;left:0;width:380px;height:50px}
.doc-dot{position:absolute;left:26px;top:13px;width:12px;height:12px;border-radius:50%}
.doc-title{position:absolute;left:61px;top:0;font-size:17px;color:var(--ink);white-space:nowrap}
.doc-date{position:absolute;left:61px;top:27px;font-size:12.5px;color:var(--muted)}
.doc-date b{color:var(--green);font-weight:700}
.doc-loc{position:absolute;left:312px;top:2px;height:28px;border-left:1px solid var(--line);padding-left:12px;display:flex;align-items:center;gap:7px;font-size:14px;font-weight:600}
.scroll-thumb{position:absolute;width:5px;border-radius:3px;background:#cfcfcf}

/* Meetings */
.meet-row{position:absolute;left:0;width:397px;height:80px}
.meet-time{position:absolute;left:23px;top:0;display:flex;align-items:center;gap:10px;font-size:21px;color:#444;font-weight:400}
.meet-time small{font-size:15px;margin-left:2px}
.meet-rule{position:absolute;left:23px;top:31px;width:125px;height:1px;background:var(--line)}
.meet-meta{position:absolute;left:23px;top:38px;display:flex;align-items:center;font-size:14px;font-weight:600;gap:6px}
.meet-meta .sep{width:1px;height:20px;background:var(--line);margin:0 10px}
.meet-divider{position:absolute;left:160px;top:2px;width:1px;height:64px;background:var(--line)}
.meet-body{position:absolute;left:171px;top:0;width:200px}
.meet-head{font-size:17px;color:var(--ink);white-space:nowrap}
.meet-desc{font-size:12.5px;color:var(--muted);line-height:16px;margin-top:4px}
.close{position:absolute;width:13px;height:13px;border-radius:50%;background:#c9c9c9;color:#fff;font-size:10px;line-height:13px;text-align:center;font-weight:700}
.see-more{position:absolute;right:10px;bottom:8px;font-size:12px;color:#333}

/* Reminders */
.rem-tabs{position:absolute;left:0;top:0;width:322px;height:45px;display:flex}
.rem-tab{flex:1;display:flex;align-items:center;justify-content:center;font-size:20px;color:#555;background:var(--tab-off);border-bottom:1px solid var(--line)}
.rem-tab.active{background:#fff;color:var(--blue);border-bottom:none;flex:0 0 166px}
.rem-item{position:absolute;left:11px;width:300px;height:45px;border:1px solid var(--line);display:flex;align-items:center;font-size:15px}
.tag{position:relative;height:22px;width:68px;margin-left:10px;margin-right:10px;background:var(--blue-tag);color:#fff;font-size:12.5px;font-weight:600;line-height:22px;padding-left:6px}
.tag::after{content:"";position:absolute;right:-9px;top:0;border-top:11px solid transparent;border-bottom:11px solid transparent;border-left:9px solid var(--blue-tag)}
.tag.alert{background:var(--red)}
.tag.alert::after{border-left-color:var(--red)}
.rem-item b{font-weight:600}
.rem-item .kind{color:var(--green);font-weight:600;margin-left:5px}
.rem-item .close{right:10px;top:15px}

/* My Latest */
.latest-head{position:absolute;left:0;top:0;width:1120px;height:56px;border-bottom:1px solid var(--line)}
.latest-title{position:absolute;left:12px;top:13px;font-size:23px;color:#3f5b80;font-weight:600}
.latest-sep{position:absolute;left:142px;top:10px;width:1px;height:32px;background:var(--line)}
.latest-date{position:absolute;left:158px;top:10px;font-size:16px;color:#555}
.latest-date big{font-size:24px;color:#333}
.today{position:absolute;left:873px;top:18px;font-size:15px;color:var(--green)}
.date-search{position:absolute;left:928px;top:10px;width:142px;height:36px;border:1px solid var(--line);background:#f6f6f6;font-size:14px;font-style:italic;color:#666;padding:8px 0 0 23px}
.go-btn{position:absolute;left:1069px;top:10px;width:40px;height:36px;background:#e1e1e1;border:1px solid #cfcfcf;font-size:14px;text-align:center;line-height:34px}
.col{position:absolute;top:56px;height:277px;border-right:1px solid var(--line)}
.col-usage{left:0;width:270px}
.col-visit{left:270px;width:277px}
.col-summary{left:547px;width:572px;border-right:none}
.col-title{position:absolute;top:34px;left:0;width:100%;text-align:center;font-size:16.5px;color:#333}
.foot-label{position:absolute;top:230px;font-size:14px;color:#333}
.val{font-weight:700}
.v-orange{color:var(--orange)}
.v-red{color:var(--red)}
.v-green{color:var(--green)}
.v-blue{color:var(--blue)}
.sum-row{position:absolute;left:23px;width:180px;font-size:14px;color:#444;display:flex;align-items:center}
.sum-row .leader{flex:1;height:1px;background:#cfcfcf;margin:0 8px}
.sum-row .pct{font-size:18px;font-weight:700;width:48px}
.mini-title{position:absolute;font-size:14px;color:#444}

/* Footer */
.footer{position:absolute;left:0;top:850px;width:1200px;height:50px;background:var(--black);color:#3c3c3c;font-size:12.5px}
.badge{position:absolute;left:26px;top:14px;width:48px;height:22px;border-radius:3px;background:#e4c42a}
.copyright{position:absolute;left:93px;top:17px}
.legal{position:absolute;right:20px;top:17px}
</style>
</head>
<body>

<header class="topbar">
  <div class="brand"><span class="brand-dot"></span><span class="brand-name">PactBloom</span></div>
  <div class="abs add-btn">+</div>
  <div class="abs nav-link" style="left:303px">Saved Search<span class="nav-caret"></span></div>
  <div class="abs nav-sep"></div>
  <div class="abs nav-link" style="left:449px">Contracts<span class="nav-caret"></span></div>
  <div class="abs nav-underline"></div>
  <svg class="abs" style="left:790px;top:28px" width="20" height="20" viewBox="0 0 20 20" aria-hidden="true"><circle cx="8" cy="8" r="6.5" fill="none" stroke="#fff" stroke-width="1.6"/><line x1="13" y1="13" x2="18.5" y2="18.5" stroke="#fff" stroke-width="1.8"/></svg>
  <svg class="abs" style="left:856px;top:26px" width="30" height="26" viewBox="0 0 30 26" aria-hidden="true"><path d="M3 3h24a2 2 0 0 1 2 2v12a2 2 0 0 1-2 2H12l-6 5v-5H3a2 2 0 0 1-2-2V5a2 2 0 0 1 2-2z" fill="#fff"/><circle cx="9" cy="11" r="2" fill="var(--blue)"/><circle cx="15" cy="11" r="2" fill="var(--blue)"/><circle cx="21" cy="11" r="2" fill="var(--blue)"/></svg>
  <div class="abs chat-badge">23</div>
  <div class="abs greet"><b>Hi,</b> Nordlane</div>
  <div class="abs avatar" role="img" aria-label="User profile photo"></div>
  <div class="abs logout"><svg width="12" height="14" viewBox="0 0 12 14" aria-hidden="true"><path d="M3 6V4a3 3 0 0 1 6 0v2" fill="none" stroke="#fff" stroke-width="1.8"/><rect x="1" y="6" width="10" height="8" rx="1" fill="#fff"/></svg>Log out</div>
  <svg class="abs" style="left:1158px;top:26px" width="24" height="24" viewBox="0 0 24 24" aria-hidden="true"><g fill="#fff"><circle cx="12" cy="12" r="8"/><rect x="10" y="0" width="4" height="24" rx="1"/><rect x="0" y="10" width="24" height="4" rx="1"/><rect x="10" y="0" width="4" height="24" rx="1" transform="rotate(45 12 12)"/><rect x="10" y="0" width="4" height="24" rx="1" transform="rotate(-45 12 12)"/></g><circle cx="12" cy="12" r="3.5" fill="var(--blue)"/></svg>
</header>

<nav class="rail">
  <div class="rail-item"><svg width="18" height="22" viewBox="0 0 18 22" aria-hidden="true"><rect x="1" y="3" width="16" height="18" rx="1" fill="#fff"/><rect x="5" y="1" width="8" height="4" rx="1" fill="#fff" stroke="var(--blue)"/><g stroke="var(--blue)" stroke-width="1.4"><line x1="4" y1="9" x2="14" y2="9"/><line x1="4" y1="13" x2="14" y2="13"/><line x1="4" y1="17" x2="14" y2="17"/></g></svg></div>
  <div class="rail-item"><svg width="22" height="18" viewBox="0 0 22 18" aria-hidden="true"><g fill="#fff"><rect x="1" y="11" width="3" height="6"/><rect x="6" y="8" width="3" height="9"/><rect x="11" y="10" width="3" height="7"/><rect x="16" y="5" width="3" height="12"/></g><polyline points="1,8 7,4 12,7 20,1" fill="none" stroke="#fff" stroke-width="1.5"/></svg></div>
  <div class="rail-item"><svg width="22" height="22" viewBox="0 0 22 22" aria-hidden="true"><circle cx="10" cy="10" r="8" fill="none" stroke="#fff" stroke-width="2"/><circle cx="10" cy="8" r="3" fill="#fff"/><path d="M5 14a5 4 0 0 1 10 0z" fill="#fff"/><line x1="16" y1="16" x2="21" y2="21" stroke="#fff" stroke-width="2.4"/></svg></div>
  <div class="rail-item"><svg width="18" height="20" viewBox="0 0 18 20" aria-hidden="true"><rect x="1" y="1" width="16" height="18" fill="none" stroke="#fff" stroke-width="1.8"/><g stroke="#fff" stroke-width="1.6"><line x1="4" y1="6" x2="14" y2="6"/><line x1="4" y1="10" x2="14" y2="10"/><line x1="4" y1="14" x2="14" y2="14"/></g></svg></div>
  <div class="rail-item"><svg width="22" height="18" viewBox="0 0 22 18" aria-hidden="true"><path d="M3 6h13v6a5 5 0 0 1-5 5H8a5 5 0 0 1-5-5z" fill="#fff"/><path d="M16 8h2a2 2 0 0 1 0 4h-2" fill="none" stroke="#fff" stroke-width="1.6"/><path d="M7 1v3M10 1v3M13 1v3" stroke="#fff" stroke-width="1.2"/></svg></div>
  <div class="rail-item"><svg width="22" height="22" viewBox="0 0 22 22" aria-hidden="true"><circle cx="9" cy="9" r="7.5" fill="none" stroke="#fff" stroke-width="2"/><line x1="14.5" y1="14.5" x2="21" y2="21" stroke="#fff" stroke-width="2.6"/><path d="M9 5v4h3" fill="none" stroke="#fff" stroke-width="1.6"/></svg></div>
</nav>

<!-- Documents -->
<section class="panel docs">
  <h2 class="panel-title" style="font-weight:400">Documents</h2>
  <div class="doc-tabs">
    <div class="doc-tab active"><svg width="14" height="18" viewBox="0 0 14 18" aria-hidden="true"><rect x="1" y="2" width="12" height="16" rx="1" fill="var(--green)"/><rect x="4" y="0.5" width="6" height="3" rx="1" fill="var(--green)" stroke="#fff"/><g stroke="#fff"><line x1="3.5" y1="8" x2="10.5" y2="8"/><line x1="3.5" y1="11" x2="10.5" y2="11"/><line x1="3.5" y1="14" x2="10.5" y2="14"/></g></svg>Contracts</div>
    <div class="doc-tab"><svg width="20" height="16" viewBox="0 0 20 16" aria-hidden="true"><g fill="#666"><rect x="1" y="10" width="3" height="6"/><rect x="6" y="7" width="3" height="9"/><rect x="11" y="9" width="3" height="7"/><rect x="16" y="4" width="3" height="12"/></g><polyline points="1,7 7,3 12,6 19,0.5" fill="none" stroke="#666" stroke-width="1.4"/></svg>Fin &amp; Adm</div>
    <div class="doc-tab"><svg width="20" height="20" viewBox="0 0 20 20" aria-hidden="true"><circle cx="9" cy="9" r="7.5" fill="none" stroke="#555" stroke-width="1.8"/><circle cx="9" cy="7.5" r="2.6" fill="#555"/><path d="M4.5 13a4.5 3.5 0 0 1 9 0z" fill="#555"/><line x1="14.5" y1="14.5" x2="19" y2="19" stroke="#555" stroke-width="2.2"/></svg>HR</div>
  </div>
  <div class="scroll-thumb" style="left:383px;top:166px;height:22px"></div>

  <div class="doc-row" style="top:175px"><span class="doc-dot" style="background:var(--red)"></span><div class="doc-title">Lorem ipsum dolor&nbsp; olor site</div><div class="doc-date"><b>20th may,</b> 10.30 am, 2016</div><div class="doc-loc"><svg width="11" height="15" viewBox="0 0 11 15" aria-hidden="true"><path d="M5.5 0A5.5 5.5 0 0 0 0 5.5C0 9.5 5.5 15 5.5 15S11 9.5 11 5.5A5.5 5.5 0 0 0 5.5 0z" fill="var(--green)"/><circle cx="5.5" cy="5.5" r="2" fill="#fff"/></svg>USA</div></div>
  <div class="doc-row" style="top:239px"><span class="doc-dot" style="background:var(--orange)"></span><div class="doc-title">Lorem ipsum dolor sit am</div><div class="doc-date"><b>22th may,</b> 10.30 am, 2016</div><div class="doc-loc"><svg width="11" height="15" viewBox="0 0 11 15" aria-hidden="true"><path d="M5.5 0A5.5 5.5 0 0 0 0 5.5C0 9.5 5.5 15 5.5 15S11 9.5 11 5.5A5.5 5.5 0 0 0 5.5 0z" fill="var(--green)"/><circle cx="5.5" cy="5.5" r="2" fill="#fff"/></svg>UAE</div></div>
  <div class="doc-row" style="top:301px"><span class="doc-dot" style="background:var(--green)"></span><div class="doc-title">Lorem ipsum dolor&nbsp; olor site</div><div class="doc-date"><b>20th may,</b> 10.30 am, 2016</div><div class="doc-loc"><svg width="11" height="15" viewBox="0 0 11 15" aria-hidden="true"><path d="M5.5 0A5.5 5.5 0 0 0 0 5.5C0 9.5 5.5 15 5.5 15S11 9.5 11 5.5A5.5 5.5 0 0 0 5.5 0z" fill="var(--green)"/><circle cx="5.5" cy="5.5" r="2" fill="#fff"/></svg>UAE</div></div>
  <div class="doc-row" style="top:366px"><span class="doc-dot" style="background:var(--blue)"></span><div class="doc-title">Lorem ipsum dolor sit am</div><div class="doc-date"><b>22th may,</b> 10.30 am, 2016</div><div class="doc-loc"><svg width="11" height="15" viewBox="0 0 11 15" aria-hidden="true"><path d="M5.5 0A5.5 5.5 0 0 0 0 5.5C0 9.5 5.5 15 5.5 15S11 9.5 11 5.5A5.5 5.5 0 0 0 5.5 0z" fill="var(--green)"/><circle cx="5.5" cy="5.5" r="2" fill="#fff"/></svg>UAE</div></div>
</section>

<!-- Meetings -->
<section class="panel meet">
  <h2 class="panel-title" style="font-weight:400">Meetings</h2>

  <div class="meet-row" style="top:72px">
    <div class="meet-time"><svg width="20" height="16" viewBox="0 0 20 16" aria-hidden="true"><path d="M1 4h13v5a5 5 0 0 1-5 5H6a5 5 0 0 1-5-5z" fill="var(--red)"/><path d="M14 6h2a2 2 0 0 1 0 4h-2" fill="none" stroke="var(--red)" stroke-width="1.5"/><rect x="0" y="14.5" width="16" height="1.5" fill="var(--red)"/></svg><span>12.30 <small>pm</small></span></div>
    <div class="meet-rule"></div>
    <div class="meet-meta"><svg width="11" height="15" viewBox="0 0 11 15" aria-hidden="true"><path d="M5.5 0A5.5 5.5 0 0 0 0 5.5C0 9.5 5.5 15 5.5 15S11 9.5 11 5.5A5.5 5.5 0 0 0 5.5 0z" fill="var(--green)"/><circle cx="5.5" cy="5.5" r="2" fill="#fff"/></svg>UAE<span class="sep"></span>25 MAY</div>
    <div class="meet-divider"></div>
    <div class="meet-body"><div class="meet-head">Lorem ipsum dolor sitr</div><div class="meet-desc">Lorem ipsum dolor sit amet,<br>consec tetuer adipiscing elit.</div></div>
    <span class="close" style="left:376px;top:6px">×</span>
  </div>

  <div class="meet-row" style="top:158px">
    <div class="meet-time"><svg width="20" height="16" viewBox="0 0 20 16" aria-hidden="true"><path d="M1 4h13v5a5 5 0 0 1-5 5H6a5 5 0 0 1-5-5z" fill="var(--orange)"/><path d="M14 6h2a2 2 0 0 1 0 4h-2" fill="none" stroke="var(--orange)" stroke-width="1.5"/><rect x="0" y="14.5" width="16" height="1.5" fill="var(--orange)"/></svg><span>05.30 <small>pm</small></span></div>
    <div class="meet-rule"></div>
    <div class="meet-meta"><svg width="11" height="15" viewBox="0 0 11 15" aria-hidden="true"><path d="M5.5 0A5.5 5.5 0 0 0 0 5.5C0 9.5 5.5 15 5.5 15S11 9.5 11 5.5A5.5 5.5 0 0 0 5.5 0z" fill="var(--green)"/><circle cx="5.5" cy="5.5" r="2" fill="#fff"/></svg>UAE<span class="sep"></span>25 MAY</div>
    <div class="meet-divider"></div>
    <div class="meet-body"><div class="meet-head">Lorem ipsum dolor sitr</div><div class="meet-desc">Lorem ipsum dolor sit amet,<br>consec tetuer.</div></div>
    <span class="close" style="left:376px;top:6px">×</span>
  </div>

  <div class="meet-row" style="top:248px">
    <div class="meet-time"><svg width="20" height="16" viewBox="0 0 20 16" aria-hidden="true"><path d="M1 4h13v5a5 5 0 0 1-5 5H6a5 5 0 0 1-5-5z" fill="var(--orange)"/><path d="M14 6h2a2 2 0 0 1 0 4h-2" fill="none" stroke="var(--orange)" stroke-width="1.5"/><rect x="0" y="14.5" width="16" height="1.5" fill="var(--orange)"/></svg><span>06.30 <small>pm</small></span></div>
    <div class="meet-rule"></div>
    <div class="meet-meta"><svg width="11" height="15" viewBox="0 0 11 15" aria-hidden="true"><path d="M5.5 0A5.5 5.5 0 0 0 0 5.5C0 9.5 5.5 15 5.5 15S11 9.5 11 5.5A5.5 5.5 0 0 0 5.5 0z" fill="var(--green)"/><circle cx="5.5" cy="5.5" r="2" fill="#fff"/></svg>USA<span class="sep"></span>25 MAY</div>
    <div class="meet-divider"></div>
    <div class="meet-body"><div class="meet-head">Lorem ipsum dolor sitr</div><div class="meet-desc">Lorem ipsum dolor sit amet,<br>consec tetuer adipi.</div></div>
    <span class="close" style="left:376px;top:6px">×</span>
  </div>

  <div class="meet-row" style="top:334px">
    <div class="meet-time"><svg width="20" height="16" viewBox="0 0 20 16" aria-hidden="true"><path d="M1 4h13v5a5 5 0 0 1-5 5H6a5 5 0 0 1-5-5z" fill="var(--orange)"/><path d="M14 6h2a2 2 0 0 1 0 4h-2" fill="none" stroke="var(--orange)" stroke-width="1.5"/><rect x="0" y="14.5" width="16" height="1.5" fill="var(--orange)"/></svg><span>05.30 <small>pm</small></span></div>
    <div class="meet-rule"></div>
    <div class="meet-meta"><svg width="11" height="15" viewBox="0 0 11 15" aria-hidden="true"><path d="M5.5 0A5.5 5.5 0 0 0 0 5.5C0 9.5 5.5 15 5.5 15S11 9.5 11 5.5A5.5 5.5 0 0 0 5.5 0z" fill="var(--green)"/><circle cx="5.5" cy="5.5" r="2" fill="#fff"/></svg>UAE<span class="sep"></span>25 MAY</div>
    <div class="meet-divider"></div>
    <div class="meet-body"><div class="meet-head">Lorem ipsum dolor sitr</div><div class="meet-desc">Lorem ipsum dolor sit amet,<br>consec.</div></div>
    <span class="close" style="left:376px;top:6px">×</span>
  </div>
  <div class="see-more">See More</div>
</section>

<!-- Reminders -->
<section class="panel rem">
  <div class="rem-tabs"><div class="rem-tab active">Reminders</div><div class="rem-tab">Activity Feed</div></div>
  <div class="rem-item" style="top:65px"><span class="tag alert">12.30 pm</span><b>25th may,</b><span class="kind">Meeting</span><span class="close">×</span></div>
  <div class="rem-item" style="top:120px"><span class="tag">05.30 pm</span><b>22th may,</b><span class="kind">Message</span><span class="close">×</span></div>
  <div class="rem-item" style="top:175px"><span class="tag">04.30 pm</span><b>21th may,</b><span class="kind">Log out</span><span class="close">×</span></div>
  <div class="rem-item" style="top:230px"><span class="tag">05.30 pm</span><b>20th may,</b><span class="kind">Up data</span><span class="close">×</span></div>
  <div class="rem-item" style="top:285px"><span class="tag">04.30 pm</span><b>19th may,</b><span class="kind">Meeting</span><span class="close">×</span></div>
  <div class="rem-item" style="top:341px"><span class="tag">04.30 pm</span><b>18th may,</b><span class="kind">Meeting</span><span class="close">×</span></div>
  <div class="see-more">See More</div>
</section>

<!-- My Latest -->
<section class="panel latest">
  <div class="latest-head">
    <h2 class="latest-title">My Latest</h2>
    <div class="latest-sep"></div>
    <div class="latest-date"><big>27</big> May, 2016</div>
    <div class="today">Today</div>
    <div class="date-search">Search by date</div>
    <div class="go-btn">Go</div>
  </div>

  <div class="col col-usage">
    <h3 class="col-title" style="font-weight:400">Monthly Usage</h3>
    <svg class="abs" style="left:0;top:0" width="270" height="230" viewBox="0 0 270 230" aria-hidden="true">
      <path d="M35 218A94 94 0 0 1 223 218L166 218A37 37 0 0 0 92 218Z" fill="#ececec"/>
      <path d="M35 218A94 94 0 0 1 100 128.6L117.6 182.8A37 37 0 0 0 92 218Z" fill="var(--red)"/>
      <path d="M127 228L106 153L135 225Z" fill="#1e1e1e"/>
      <line x1="16" y1="218.5" x2="244" y2="218.5" stroke="#cfcfcf"/>
    </svg>
    <div class="foot-label" style="left:17px">Total</div>
    <div class="foot-label val v-orange" style="left:110px">1,026</div>
    <div class="foot-label val v-red" style="left:214px">40%</div>
  </div>

  <div class="col col-visit">
    <h3 class="col-title" style="font-weight:400">Visitor per day</h3>
    <span class="abs" style="left:20px;top:40px;width:15px;height:15px;border-radius:50%;background:#d2d2d2;color:#fff;font-size:10px;line-height:15px;text-align:center">‹</span>
    <span class="abs" style="left:243px;top:40px;width:15px;height:15px;border-radius:50%;background:var(--orange);color:#fff;font-size:10px;line-height:15px;text-align:center">›</span>
    <svg class="abs" style="left:0;top:0" width="277" height="230" viewBox="0 0 277 230" aria-label="Visitors per day line chart" role="img">
      <defs><linearGradient id="visitFill" x1="0" y1="0" x2="0" y2="1"><stop offset="0" stop-color="#f9d9b4"/><stop offset="1" stop-color="#fff6ec" stop-opacity="0"/></linearGradient></defs>
      <g font-size="11.5" fill="#333" font-family="Open Sans, sans-serif">
        <text x="18" y="114">100%</text><text x="24" y="147">50%</text><text x="30" y="180">0%</text>
        <text x="26" y="207" fill="var(--green)" font-weight="600">May</text>
        <text x="64" y="207">0</text><text x="106" y="207">5</text><text x="142" y="207">10</text><text x="181" y="207">15</text><text x="224" y="207">20</text>
      </g>
      <g stroke="#dedede"><line x1="61" y1="110" x2="238" y2="110"/><line x1="61" y1="143" x2="238" y2="143"/><line x1="61" y1="176" x2="238" y2="176"/></g>
      <path d="M70 176L101 144L122 159L152 126L179 153L203 137L203 176Z" fill="url(#visitFill)"/>
      <polyline points="70,176 101,144 122,159 152,126 179,153 203,137" fill="none" stroke="#7ac143" stroke-width="4" stroke-linejoin="round"/>
      <g fill="#fff" stroke="var(--red)" stroke-width="3"><circle cx="101" cy="144" r="6"/><circle cx="152" cy="126" r="6"/><circle cx="203" cy="137" r="6"/></g>
      <line x1="15" y1="219.5" x2="262" y2="219.5" stroke="#cfcfcf"/>
    </svg>
    <div class="foot-label val v-orange" style="left:27px">1,026</div>
    <div class="foot-label val v-blue" style="left:208px">↑ 10%</div>
  </div>

  <div class="col col-summary">
    <h3 class="col-title" style="font-weight:400">Last Month Summery</h3>
    <div class="scroll-thumb" style="left:554px;top:16px;height:24px"></div>
    <div class="sum-row" style="top:102px;width:226px">Contracts<span class="leader"></span><span class="pct v-red">66 %</span></div>
    <div class="sum-row" style="top:136px;width:226px">Finance &amp; Admin<span class="leader"></span><span class="pct v-green">47 %</span></div>
    <div class="sum-row" style="top:168px;width:226px">HR<span class="leader"></span><span class="pct v-orange">5 %</span></div>

    <div class="mini-title" style="left:252px;top:102px">Remainder</div>
    <svg class="abs" style="left:250px;top:125px" width="80" height="72" viewBox="0 0 80 72" aria-hidden="true">
      <path d="M3 41A37 37 0 0 1 77 41L52 41A12 12 0 0 0 28 41Z" fill="#ececec"/>
      <path d="M3 41A37 37 0 0 1 28.6 5.8L36.3 29.6A12 12 0 0 0 28 41Z" fill="var(--red)"/>
      <path d="M39 43L33 18L42 42Z" fill="#1e1e1e"/>
      <text x="40" y="66" text-anchor="middle" font-size="13" font-weight="600" fill="#333" font-family="Open Sans, sans-serif">40%</text>
    </svg>

    <div class="mini-title" style="left:401px;top:102px">Daily activity</div>
    <span class="abs" style="left:364px;top:151px;width:15px;height:15px;border-radius:50%;background:#d2d2d2;color:#fff;font-size:10px;line-height:15px;text-align:center">‹</span>
    <span class="abs" style="left:518px;top:151px;width:15px;height:15px;border-radius:50%;background:var(--orange);color:#fff;font-size:10px;line-height:15px;text-align:center">›</span>
    <svg class="abs" style="left:385px;top:130px" width="130" height="66" viewBox="0 0 130 66" aria-label="Daily activity bar chart" role="img">
      <g fill="#e4e4e4"><rect x="5" y="6" width="13" height="40"/><rect x="32" y="6" width="13" height="40"/><rect x="53" y="6" width="13" height="40"/><rect x="74" y="6" width="13" height="40"/><rect x="95" y="6" width="13" height="40"/><rect x="117" y="6" width="13" height="40"/></g>
      <g fill="#7ac143"><rect x="5" y="27" width="13" height="19"/><rect x="32" y="18" width="13" height="28"/><rect x="53" y="34" width="13" height="12"/><rect x="74" y="18" width="13" height="28"/><rect x="95" y="18" width="13" height="28"/><rect x="117" y="32" width="13" height="14"/></g>
      <g font-size="10" font-weight="700" fill="#333" text-anchor="middle" font-family="Open Sans, sans-serif"><text x="11.5" y="60">1</text><text x="38.5" y="60">2</text><text x="59.5" y="60">3</text><text x="80.5" y="60">4</text><text x="101.5" y="60">5</text><text x="123.5" y="60">6</text></g>
    </svg>

    <svg class="abs" style="left:0;top:0" width="572" height="230" aria-hidden="true"><line x1="20" y1="218.5" x2="545" y2="218.5" stroke="#cfcfcf"/></svg>
    <div class="foot-label" style="left:23px">Total <span class="val v-orange" style="margin-left:6px">22,026</span></div>
    <div class="foot-label val v-blue" style="left:496px">↑ 22%</div>
  </div>
</section>

<footer class="footer">
  <div class="badge"></div>
  <div class="copyright">Copyright © 2016 PactBloom Ltd</div>
  <div class="legal">Terms of Use Privacy</div>
</footer>

</body>
</html>
```